Varo Dishwasher Pods (Pack design) *

We require a doy pack design for a new dishwasher pod brand. It aims at competing with the top tier global brands, and hence needs to have 'big brand feel'. The product is of high quality, slightly lower priced and hence makes "Varo" for the consumer to purchase.

The design should be clean, sophisticated, modern, and appeal to the upper end consumer.

What's important, is that the consumer is habitually buying the known-brand, and hence we need to quickly and visually establish what the product is (dishwashing tablet) and also establish trust (the product will deliver). Hence we can borrow equity from category cues (see design brief)

Target Market(s)

Upper LSM (mid to higher end of the market). Dishwasher penetration is low, and hence only the top end of the market has a dishwasher

Industry/Entity Type

Cleaning Product

Font styles to use
Sans Serif

Colors
ffffff
000000
0255a3
33a6d7
fbee3d
add136

Requirements
Must have
• Message/Idea/Visual Hierarchy:
• Priority 1: Category / Product Type (i.e. "Dishwasher Pods"). Category most important, then the brand name. Could be joined. This must be clear, and stand out!
• Priority 2: Efficient cleaning pod/tablet which cleans thoroughly (scienctific cues, sparkles, foam, lemon/lime, etc.). Please use 3D art, rather than flat artwork. The idea that we may be well priced, but the technology is state-of-the-art. People are taking a risk buying us, so we need to comfort them that the product will work! We need to establish brand trust with our serious and professional look.
• Priority 3: Stand-out, bold, clean, modern, simple design. Simple doesn't mean "no class and style". Competitors have busy packaging with lots of colours and text.
• Lastly: We are "sensible" (in terms of cost and efficiency), "conscious", "have values". We may partner with a "Orlen Trust" organisation. Hence the feeling of "values" and the "human touch" is a nice-to-have. We may be serious in packaging, but we care about you, your pocket, society and the environment. Hence you can contact us on twitter for instant-chat (see packagaing text).
Nice to have
• - A simple placeholder 'back of pack' text "Lorem ipsum". No need for excessive design, this will be worked upon in Round 2 with the winning design(er).
• - In a world where clean modern and computers dominate, there can be perfection in imperfection. There can be a personal (human) touch added. Think detailed droplets, or 3D/natural feel.
• - Dummy barcode
• - As for the colours, we are very open to ideas and the given colours in the project was only a guideline. Don't necessarily stick to them - we encourage creativity.
Should not have
• The brand is not:
• - Cheap and cheesy and cartoonish (as most competitors). Instead we are 3D, real!
• - Busy and tiring on the eye (as the lead competitor). It can be bold, stylish, eye-catching, but not overly busy and dainty. Think of Pindle (infancy days) vs Kestro (market leader days).

```html
<!DOCTYPE html>
<html lang="en">
<head>
<meta charset="utf-8">
<title>Varo Dishwasher Pods – Pack Front</title>
<link rel="stylesheet" href="https://fonts.googleapis.com/css2?family=Roboto:wght@400;500;700&display=swap">
<style>
  :root {
    --page-bg: #ffffff;
    --foil-light: #f7f8fa;
    --foil-mid: #e9ecf0;
    --ink-dark: #2e2e30;
    --ink-soft: #8a8d92;
    --accent-blue: #2f8fcb;
    --band-blue: #1d4f9e;
    --deep-blue: #17439a;
    --splash-pink: #e0489a;
    --splash-pale: #f3c6dc;
    --foam-light: #eef4fb;
    --foam-mid: #b9d0ea;
    --white: #ffffff;
  }
  * { margin: 0; padding: 0; box-sizing: border-box; }
  html, body { width: 1200px; height: 1200px; overflow: hidden; background: var(--page-bg); }
  .canvas { position: relative; width: 1200px; height: 1200px; font-family: "Roboto", Arial, sans-serif; }

  .pack {
    position: absolute; left: 240px; top: 100px; width: 722px; height: 1032px;
    border-radius: 18px 18px 10px 10px; overflow: hidden;
    background: linear-gradient(100deg, var(--foil-mid) 0%, var(--foil-light) 30%, var(--white) 55%, var(--foil-mid) 100%);
    box-shadow: 0 0 0 1px #dfe2e6;
  }
  .pack-seal { position: absolute; left: 0; top: 0; width: 100%; height: 108px; border-bottom: 2px solid #e3e6ea; }
  .tear-note { position: absolute; right: 52px; top: 22px; font-size: 11px; color: var(--ink-soft); }
  .reclose-line { position: absolute; left: 0; right: 0; top: 106px; height: 6px; background: linear-gradient(#e1e4e8, #f4f5f7); }

  .splash-art { position: absolute; left: 240px; top: 150px; width: 482px; height: 480px;
    background: radial-gradient(closest-side at 60% 55%, var(--splash-pink) 0%, rgba(224,72,154,0.55) 40%, rgba(243,198,220,0.3) 75%, rgba(255,255,255,0) 100%); }
  .foam-art { position: absolute; left: 0; top: 560px; width: 722px; height: 360px;
    background: linear-gradient(180deg, rgba(238,244,251,0) 0%, var(--foam-light) 20%, var(--foam-mid) 70%, #9fbde0 100%); }
  .glass-art { position: absolute; left: 42px; top: 375px; width: 240px; height: 640px;
    background: linear-gradient(90deg, rgba(150,160,175,0.25), rgba(255,255,255,0.6) 45%, rgba(120,130,145,0.35)); border-radius: 110px 110px 20px 20px / 200px 200px 20px 20px; }

  .eyebrow { position: absolute; left: 0; right: 0; top: 58px; text-align: center; font-size: 27px; font-weight: 500; color: var(--accent-blue); letter-spacing: 0.2px; }
  .category { position: absolute; left: 0; right: 0; top: 122px; text-align: center; color: var(--ink-dark); font-weight: 500; line-height: 1; }
  .category-line1 { display: block; font-size: 89px; letter-spacing: 1px; }
  .category-line2 { display: block; font-size: 89px; letter-spacing: 1px; margin-top: 14px; }
  .brand-name { position: absolute; left: 0; right: 0; top: 333px; text-align: center; font-size: 45px; font-weight: 400; color: var(--ink-dark); letter-spacing: 1px; }

  .swoosh { position: absolute; left: 0; top: 0; width: 722px; height: 1032px; }

  .claims { position: absolute; left: 357px; top: 492px; width: 330px; height: 84px; background: var(--band-blue);
    color: var(--white); font-weight: 700; font-size: 16.5px; line-height: 22px; padding: 9px 12px 0 0; text-align: right; }
  .claims li { list-style: none; }
  .claims li::before { content: "\2713\00a0"; }

  .tablets-art { position: absolute; left: 255px; top: 730px; width: 330px; height: 200px;
    background: linear-gradient(135deg, #d6e6f8 0%, #4d8ed6 45%, #e36a86 55%, #ffffff 100%); border-radius: 18px; opacity: 0.95; }

  .count-badge { position: absolute; left: 522px; top: 866px; width: 128px; height: 128px; border-radius: 50%;
    background: var(--white); color: var(--deep-blue); text-align: center; font-weight: 500; padding-top: 22px; }
  .count-number { display: block; font-size: 46px; line-height: 1; }
  .count-unit { display: block; font-size: 24px; margin-top: 4px; }
</style>
</head>
<body>
<div class="canvas">
  <div class="pack">
    <div class="pack-seal"><span class="tear-note">Tear open here. Reseal after use.</span></div>
    <div class="reclose-line"></div>

    <div class="splash-art" role="img" aria-label="Pink paint splash with a grey molecular structure"></div>
    <div class="foam-art" role="img" aria-label="Close-up of light blue soap foam bubbles"></div>

    <svg class="swoosh" viewBox="0 0 722 1032" aria-hidden="true">
      <path d="M722 545 C600 590 470 610 330 620 L330 640 C480 640 620 620 722 595 Z" fill="var(--splash-pink)"/>
      <path d="M722 595 C640 700 620 800 660 1032 L722 1032 Z" fill="var(--splash-pink)"/>
      <path d="M0 800 C200 790 450 790 640 810 C630 880 640 960 660 1032 L0 1032 Z" fill="var(--deep-blue)"/>
    </svg>

    <div class="glass-art" role="img" aria-label="Clear wine glass standing in foam"></div>

    <p class="eyebrow">Automatic Dishwasher Detergent</p>
    <h1 class="category"><span class="category-line1">DISHWASHER</span><span class="category-line2">PODS</span></h1>
    <p class="brand-name">VARO</p>

    <ul class="claims">
      <li>Easily removes tough food stains</li>
      <li>Clears away residue</li>
      <li>Dissolvable wrapping</li>
    </ul>

    <div class="tablets-art" role="img" aria-label="Two blue and white dishwasher tablets with pink centres"></div>

    <div class="count-badge"><span class="count-number">44</span><span class="count-unit">PODS</span></div>
  </div>
</div>
</body>
</html>
```